Founder / concept developer needs business card // Consultant needs VCARD

I need a business card for me as a founding consultant in Berlin. I advise entrepreneurs, especially in the design of business ideas, business plans or financing applications. More information about this in the annexes. My USP: I design / structure complex ideas and projects convincingly so that my client is successful. I want to communicate professionalism, effectiveness and clarity. Colors like from the range BLACK-GRAY-GREEN. I am 27 years old, I have studied business for 7 years. Attachments: - Business card design (only idea, do not focus on it) - Website screenshot (only idea, do not focus on it)

Target Market(s)

Target group: Founder (20-50 yrs, m / w, needy, in "break-up phase") and CONTRACTOR / "financier" (30-55 yrs, m / w, often public service "routine-oriented"). The foundations are in quite different industries: digital, craft, tourism, retail, services, etc. Almost all German.

Industry/Entity Type

Consultant

Contact Information for Business Card

Lukas Brandvik
M. Sc., International Business Administration
Gründungsberater, Konzeptentwickler
www.falkenhorn-beratung.de
kontakt@falkenhorn-beratung.de
Tel. 0471 239 5518

Colors

Designer to choose colors to be used in the design.

Requirements
Must have
• Professionalism, persuasiveness, clarity
Nice to have
• memorability
Should not have
• Schnörkelei

```html
<!DOCTYPE html>
<html lang="de">
<head>
<meta charset="utf-8">
<title>Lukas Brandvik – Visitenkarte</title>
<link rel="stylesheet" href="https://fonts.googleapis.com/css2?family=Michroma&family=Roboto+Condensed:wght@400&family=Titillium+Web:wght@200;300&display=swap">
<style>
  :root {
    --stage: #d9d9d6;
    --paper: #eeece0;
    --charcoal: #2c2927;
    --navy: #0f4266;
    --ink: #4a4846;
    --ink-soft: #8d8a84;
    --white: #ffffff;
  }
  * { box-sizing: border-box; margin: 0; padding: 0; }
  html, body { width: 1200px; height: 786px; overflow: hidden; }
  body {
    background: var(--stage);
    position: relative;
    font-family: "Titillium Web", sans-serif;
  }
  .card {
    position: absolute;
    top: 243px;
    width: 500px;
    height: 300px;
    overflow: hidden;
    box-shadow: 0 6px 18px rgba(0,0,0,0.18);
  }
  .card--front { left: 70px; background: var(--paper); }
  .card--back { left: 630px; background: var(--charcoal); }

  .contact {
    position: absolute;
    top: 50px;
    left: 10px;
    width: 250px;
    text-align: right;
    color: var(--ink);
    font-weight: 300;
    font-size: 15px;
    line-height: 19px;
    text-transform: uppercase;
    letter-spacing: 0.02em;
    white-space: nowrap;
  }
  .contact .email, .contact .web { font-size: 12.5px; line-height: 17px; }

  .name-band {
    position: absolute;
    top: 140px;
    left: 200px;
    right: 0;
    height: 46px;
    background: var(--navy);
    display: flex;
    align-items: center;
    padding-left: 26px;
  }
  .name {
    font-family: "Michroma", sans-serif;
    font-weight: 400;
    color: var(--white);
    font-size: 18px;
    letter-spacing: 0.02em;
    white-space: nowrap;
  }
  .credentials {
    position: absolute;
    top: 196px;
    left: 178px;
    font-family: "Roboto Condensed", sans-serif;
    font-size: 12.5px;
    line-height: 16px;
    color: var(--ink);
    white-space: nowrap;
  }

  .brand-square {
    position: absolute;
    top: 52px;
    left: 78px;
    width: 104px;
    height: 78px;
    background: var(--navy);
    display: flex;
    align-items: center;
    justify-content: center;
  }
  .brand-name {
    color: var(--white);
    font-weight: 300;
    font-size: 16px;
    letter-spacing: 0.08em;
    text-transform: uppercase;
  }
  .site {
    position: absolute;
    top: 178px;
    left: 0;
    right: 0;
    text-align: center;
    color: var(--ink-soft);
    font-weight: 200;
    font-size: 15px;
    letter-spacing: 0.32em;
    text-transform: uppercase;
    white-space: nowrap;
  }
</style>
</head>
<body>
  <section class="card card--front" aria-label="Vorderseite">
    <div class="contact">
      <p class="phone">0471 239 5518</p>
      <p class="email">kontakt@falkenhorn-beratung.de</p>
      <p class="web">www.falkenhorn-beratung.de</p>
    </div>
    <div class="name-band"><h1 class="name">LUKAS BRANDVIK</h1></div>
    <div class="credentials">
      <p>M. Sc., International Business Administration</p>
      <p>Gründungsberater, Konzeptentwickler</p>
    </div>
  </section>

  <section class="card card--back" aria-label="Rückseite">
    <div class="brand-square"><span class="brand-name">Brandvik</span></div>
    <p class="site">www.falkenhorn-beratung.de</p>
  </section>
</body>
</html>
```